Quillmere Finance

We need a corporate style website design for a new company based in Shenzhen's Qianhai Special Economic Development Zone, China. We provide a range of financial services to large international investment companies. Typically these companies invest over 5 million RMB. The company is part of a group that consists of LumaBuilders, CorvelHoldings and CorvelAssets. Our location and gateway into Qianhai Special Economic Zone is our core advantage. We would like to see designs that Do Not use purple and orange. The website design should be similar to other websites in this family but different enough to give it a unique style (See attached website links for reference). The final design should communicate financial safety and growth. This website will act partly as a business chamber with connections to the government so we would like it to be diplomatic in style.

www.lumabuilders-example.com
www.corvelholdings-example.com

*Nevegation Bar
Should including Homepage, Financial Product, Team, News.
Could refer to www.corvelholdings-example.com

*Contact Details

Miss Tan
Address:E 227, North Block, ODX Building, East Sector, Shenzhen Brightfield Science Park
Telephone: +86 0755 20473915
Cellphone: +86 13907582216

* Social Media
Should be grouped like:
1. Weibo QRcode+ Weibo
2. Facebook, Twitter, Linkedin.

Industry/Entity Type

Investment

```html
<!DOCTYPE html>
<html lang="en">
<head>
<meta charset="utf-8">
<title>Quillmere Finance</title>
<link rel="stylesheet" href="https://fonts.googleapis.com/css2?family=Roboto:ital,wght@0,300;0,400;0,500;1,400;1,500&family=Roboto+Condensed:wght@400;700&family=Tinos:wght@400;700&display=swap">
<style>
:root{
  --navy:#0d4a8a;
  --navy-dark:#0a3566;
  --ink:#222;
  --rule:#cfcfcf;
  --panel:#c8c8c8;
  --white:#fff;
  --black:#000;
}
*{box-sizing:border-box;margin:0;padding:0}
html,body{width:1062px;height:1200px;overflow:hidden;background:var(--white);font-family:"Roboto",sans-serif;color:var(--ink)}
.page{position:relative;width:1062px;height:1200px}
.hero{position:absolute;left:0;top:0;width:1062px;height:456px;
  background:linear-gradient(180deg,#3a2f35 0%,#5a5560 35%,#6b6a70 60%,#4a3b30 85%,#2c2a35 100%)}
.hero-shade{position:absolute;inset:0;background:rgba(20,20,40,.35)}
.brand{position:absolute;left:58px;top:15px;width:166px;height:54px;background:rgba(0,0,0,.55);
  display:flex;align-items:center;justify-content:center;color:#aaa;font-size:10px;letter-spacing:2.5px;font-weight:500}
.lang{position:absolute;left:865px;top:16px;width:83px;height:19px;border:1px solid #aaa;background:rgba(255,255,255,.15);
  color:#eee;font-size:9px;font-style:italic;padding:3px 8px}
.social{position:absolute;top:19px;width:20px;height:20px;border-radius:50%;background:#bbb}
.nav{position:absolute;right:58px;top:53px;display:flex;gap:22px;list-style:none}
.nav li{font-family:"Roboto Condensed",sans-serif;font-weight:700;font-size:11.5px;color:#fff;padding-bottom:3px}
.nav li.active{border-bottom:2px solid #fff}
.hero h1{position:absolute;top:176px;left:0;width:100%;text-align:center;color:#fff;font-weight:500;font-size:48px;letter-spacing:-.5px}
.hero p{position:absolute;top:248px;left:0;width:100%;text-align:center;color:#fff;font-weight:300;font-size:16.5px;line-height:25px}
.hero-btn{position:absolute;left:427px;top:311px;width:208px;height:41px;border-radius:5px;
  background:linear-gradient(180deg,#1a63b0,var(--navy-dark));color:#fff;font-family:"Tinos",serif;font-weight:700;font-size:14px;
  display:flex;align-items:center;justify-content:center;gap:8px}
.arrow{position:absolute;top:245px}
.notch{position:absolute;left:523px;top:456px}
.dots{position:absolute;top:477px;left:510px;display:flex;gap:9px}
.dots span{width:8px;height:8px;border-radius:50%;background:#ccc}
.dots span.on{background:var(--navy)}
.section{position:absolute;left:66px;width:615px}
.section h2{font-family:"Tinos",serif;font-weight:400;font-size:24px;color:var(--navy);letter-spacing:.3px}
.section h2 b{font-weight:700}
.section .bar{width:105px;height:3px;border-top:1px solid var(--rule);border-bottom:1px solid var(--rule);margin-top:7px}
.section p{margin-top:20px;width:590px;font-size:11px;line-height:20.8px;font-weight:300;color:#333}
.more{margin-top:19px;display:flex;align-items:flex-end;border-bottom:1px solid var(--rule)}
.more span{display:inline-block;width:104px;height:33px;background:linear-gradient(180deg,#1a63b0,var(--navy-dark));
  color:#fff;font-family:"Tinos",serif;font-weight:700;font-size:12px;line-height:33px;text-align:center}
.contact-head{position:absolute;left:697px;top:596px;height:33px;width:299px;background:var(--panel);border-left:4px solid var(--navy);
  clip-path:polygon(0 0,100% 0,94% 100%,0 100%);font-family:"Tinos",serif;font-size:16px;padding:9px 13px;letter-spacing:.3px}
.intro{position:absolute;left:714px;top:650px;width:266px;font-style:italic;font-weight:500;font-size:12.4px;line-height:21.5px}
.rows{position:absolute;left:714px;top:724px;width:266px;border-top:3px double var(--rule);list-style:none}
.rows li{display:flex;gap:10px;align-items:flex-start;border-bottom:1px solid var(--rule);padding:12px 0 11px;color:var(--navy);font-size:16px;font-weight:300;line-height:21px;white-space:nowrap}
.rows li.wrap{white-space:normal}
.rows svg{flex:none;margin-top:1px}
.footer{position:absolute;left:0;top:1061px;width:1062px;height:139px;background:var(--black);color:#ddd}
.footer ul{list-style:none;display:flex;justify-content:center;gap:11px;margin-top:31px}
.footer li{font-family:"Roboto Condensed",sans-serif;font-weight:700;font-size:11px}
.footer small{display:block;text-align:center;margin-top:8px;font-family:"Tinos",serif;font-size:9.5px}
</style>
</head>
<body>
<div class="page">
  <header class="hero" role="img" aria-label="Aerial photograph of Qianhai skyline with towers and waterfront">
    <div class="hero-shade"></div>
    <div class="brand">QUILLMERE FINANCE</div>
    <div class="lang">English</div>
    <span class="social" style="left:960px"></span>
    <span class="social" style="left:984px"></span>
    <ul class="nav">
      <li class="active">HOME</li><li>ABOUT US</li><li>OUR SERVICES</li><li>EXPERT TEAM</li>
      <li>PARTNERS</li><li>NEWS</li><li>JOIN US</li><li>CONTACT US</li>
    </ul>
    <h1>ACHIEVE DREAMS IN QIANHAI</h1>
    <p>Lorem ipsum dolor sit amet, consectetur adipiscing elit. Proin egestas auctor sapien sit amet elementum.<br>Aenean nec tincidunt nunc, euismod faucibus nisl. Etiam luctus, magna et pellentesque eleifend.</p>
    <div class="hero-btn">Learn What We Can Do
      <svg width="10" height="12" viewBox="0 0 10 12"><path d="M2 1l5 5-5 5" stroke="#fff" stroke-width="2.5" fill="none"/></svg>
    </div>
    <svg class="arrow" style="left:25px" width="34" height="68" viewBox="0 0 34 68"><path d="M33 1L1 34l32 33" stroke="#fff" stroke-width="1.2" fill="none"/></svg>
    <svg class="arrow" style="left:1004px" width="34" height="68" viewBox="0 0 34 68"><path d="M1 1l32 33L1 67" stroke="#fff" stroke-width="1.2" fill="none"/></svg>
  </header>
  <svg class="notch" width="16" height="9" viewBox="0 0 16 9"><path d="M0 0h16L8 9z" fill="#3a3440"/></svg>
  <div class="dots"><span></span><span class="on"></span><span></span></div>

  <section class="section" style="top:591px">
    <h2>WELCOME TO <b>QUILLMERE FINANCE</b></h2>
    <div class="bar"></div>
    <p>Lorem ipsum dolor sit amet, consectetur adipiscing elit. Phasellus facilisis et purus at tincidunt. Aliquam viverra malesuada faucibus. Phasellus sagittis molestie mi sit amet porttitor. Interdum et malesuada fames ac ante ipsum primis in faucibus. Sed et sodales magna. Etiam sed pellentesque magna. Vivamus auctor quis nisi a sodales. Morbi volutpat tortor vel ipsum dapibus rutrum. Etiam elit felis, cursus eleifend eleifend at, vehicula eu lorem.</p>
    <div class="more"><span>Learn More »</span></div>
  </section>

  <section class="section" style="top:846px">
    <h2>OUR <b>SERVICES</b></h2>
    <div class="bar"></div>
    <p>In sed gravida nunc. Quisque tristique, purus in fermentum ullamcorper, purus elit vulputate ipsum, vel tempor erat sapien sit amet velit. Pellentesque iaculis et elit vitae faucibus. Sed elit nulla, volutpat malesuada commodo ut, consequat non orci. Suspendisse feugiat congue massa, eu mattis nibh porttitor molestie. Integer eget felis dignissim nunc tincidunt laoreet. Proin egestas sem eu diam egestas consequat. Praesent purus nisl, tincidunt vitae enim</p>
    <div class="more"><span>Learn More »</span></div>
  </section>

  <aside>
    <div class="contact-head">GET IN TOUCH</div>
    <p class="intro">Lorem ipsum dolor sit amet, consectetur adip iscing elit. Phasellus facilisis et purus at tincdunt. Aliquam viverra malesuada faucibus.</p>
    <ul class="rows">
      <li><svg width="30" height="22" viewBox="0 0 30 22"><path d="M2 8c0-4 6-6 13-6s13 2 13 6v2h-6V7H8v3H2z" fill="var(--navy)"/><rect x="6" y="11" width="18" height="10" rx="2" fill="var(--navy)"/><g fill="#fff"><rect x="10" y="13" width="2" height="2"/><rect x="14" y="13" width="2" height="2"/><rect x="18" y="13" width="2" height="2"/><rect x="10" y="17" width="2" height="2"/><rect x="14" y="17" width="2" height="2"/><rect x="18" y="17" width="2" height="2"/></g></svg>+86 0755 20473915</li>
      <li><svg width="30" height="20" viewBox="0 0 30 20"><rect x="1" y="1" width="28" height="18" fill="none" stroke="var(--navy)" stroke-width="2"/><path d="M1 1l14 11L29 1M1 19l10-9M29 19l-10-9" stroke="var(--navy)" stroke-width="2" fill="none"/></svg>info@quillmere.example</li>
      <li><svg width="30" height="22" viewBox="0 0 30 22"><circle cx="15" cy="6" r="5.5" fill="var(--navy)"/><path d="M3 22c0-7 5-10 12-10s12 3 12 10z" fill="var(--navy)"/></svg>mstan@quillmere.example</li>
      <li class="wrap"><svg width="30" height="26" viewBox="0 0 30 26"><path d="M15 1a9 9 0 0 0-9 9c0 7 9 15 9 15s9-8 9-15a9 9 0 0 0-9-9z" fill="var(--navy)"/><circle cx="15" cy="10" r="3.5" fill="#fff"/></svg><span>E 227, North Block, ODX Building, East Sector, Shenzhen Brightfield Science Park</span></li>
    </ul>
  </aside>

  <footer class="footer">
    <ul>
      <li>HOME</li><li>:</li><li>ABOUT US</li><li>:</li><li>OUR SERVICES</li><li>:</li><li>EXPERT TEAM</li><li>:</li>
      <li>PARTNERS</li><li>:</li><li>NEWS</li><li>:</li><li>JOIN US</li><li>:</li><li>CONTACT US</li>
    </ul>
    <small>@2014 Quillmere Finance. All Rights Reserved.</small>
  </footer>
</div>
</body>
</html>
```